Business Card & Logo Design - Hedge Fund

We need a business card and logo design for a hedge fund. The hedge fund is named Morvane Equity LLC. Morvane Equity was created by finance professors and the strategy is based academic research that looks for patterns in stock prices. The design should look conservative, solid, strong. We favor a classic style - nothing flashy. The logo can relate to the name Morvane Equity, or it could involve a symbol design that connotes "science" . We are open to ideas. We do not want alot of colors - but if any, color - blue is preferred. The font that seems to look best for the name (Morvane Equity) is arial black. We are open to ideas. Most important - we want to see a mock up of an actual business card with the logo concept embedded. The business card should include space for : company name, individual name, position title, cell phone, address. We hope to have this work done by Sept. 8.

Target Market(s)

We will be meeting with and giving the business card to institutions and high net worth individuals.

Industry/Entity Type

Investment Advisory

Contact Information for Business Card

Company name - Morvane Equity LLC
Individual name - Peter Dalby
Title - Portfolio Manager
Cell - (412) 555-0187
Address - 2650 Birchmont Lane, Suite 300, Atlanta GA 30327

Font styles to use
Other font styles liked:
• Arial

Colors
3277b5
0255a3
85acd3
cedeed
fdf9cf
d9d9d9
e6e6e6
f04a50
6b449b

Requirements
Must have
• Must have card details that are sited above.
• We would like a logo related to the name (Morvane Equity) or concept of the fund.
Nice to have
• We want conservative / understated / clean crisp look.
• If any colors - we prefer conservative appearance - blue / gray.
• I have enclosed an example of a card style that looks attractive - please do not exactly copy this card. This is not our company or logo. I feel the layout is attractive - just as an example
Should not have
• Avoid too much color.
• I have selected some preferred colors. Please do not use all of the colors - I have selected a few that might work - but I am not sure. We are open to your ideas so please do not feel the need to use all or any of these.

```html
<!DOCTYPE html>
<html lang="en">
<head>
<meta charset="utf-8">
<title>Morvane Equity LLC – Business Card</title>
<link rel="stylesheet" href="https://fonts.googleapis.com/css2?family=Work+Sans:wght@400;500;700&display=swap">
<style>
  :root {
    --backdrop: #2b2b2c;
    --card: #1c1c1d;
    --card-edge: #262627;
    --ink: #ffffff;
    --ink-soft: #e6e6e6;
    --silver-light: #e9e9e9;
    --silver-mid: #9a9a9a;
    --silver-dark: #3a3a3b;
    --gloss: #2f2f30;
  }
  * { box-sizing: border-box; margin: 0; padding: 0; }
  html, body {
    width: 1200px; height: 900px; overflow: hidden;
    background: var(--backdrop);
    font-family: "Work Sans", Arial, sans-serif;
  }
  .canvas {
    position: relative; width: 1200px; height: 900px;
  }
  .card {
    position: absolute; left: 270px; width: 660px; height: 377px;
    background: var(--card);
    border: 1px solid var(--card-edge);
    box-shadow: 0 18px 40px rgba(0,0,0,.45);
    overflow: hidden;
  }
  .card--back { top: 48px; }
  .card--front { top: 475px; }

  .wordmark {
    display: flex; align-items: center; gap: 10px;
    font-weight: 700; white-space: nowrap;
  }
  .wordmark__dot {
    border-radius: 50%; flex: none;
  }
  .card--back .wordmark {
    position: absolute; left: 0; right: 0; top: 160px;
    justify-content: center;
    font-size: 40px; color: var(--gloss);
    letter-spacing: .5px;
  }
  .card--back .wordmark__dot {
    width: 30px; height: 30px; background: var(--gloss);
  }

  .card--front .wordmark {
    position: absolute; left: 40px; top: 38px;
    font-size: 24px; color: var(--ink);
  }
  .card--front .wordmark__dot {
    width: 18px; height: 18px; background: var(--ink);
  }

  .person { position: absolute; left: 56px; top: 118px; }
  .person__name {
    font-size: 27px; font-weight: 500; letter-spacing: 2.5px;
    color: var(--ink); line-height: 1.1;
  }
  .person__title {
    font-size: 15px; color: var(--ink-soft); letter-spacing: .5px; margin-top: 2px;
  }
  .address {
    position: absolute; left: 56px; top: 196px;
    font-size: 16px; line-height: 1.45; color: var(--ink); letter-spacing: .3px;
  }
  .contacts {
    position: absolute; left: 40px; top: 262px;
    list-style: none; font-size: 17px; color: var(--ink); letter-spacing: .3px;
  }
  .contacts__item { display: flex; align-items: center; gap: 10px; line-height: 1.5; }
  .contacts__icon { width: 12px; height: 12px; flex: none; }

  .emblem {
    position: absolute; right: 60px; top: 80px;
    width: 230px; height: 230px; border-radius: 50%;
    background: linear-gradient(135deg, var(--silver-dark) 0%, var(--silver-mid) 55%, var(--silver-light) 100%);
  }
</style>
</head>
<body>
<main class="canvas">

  <section class="card card--back" aria-label="Card back">
    <div class="wordmark">
      <span class="wordmark__dot"></span>
      <span class="wordmark__name">Morvane Equity LLC</span>
    </div>
  </section>

  <section class="card card--front" aria-label="Card front">
    <div class="wordmark">
      <span class="wordmark__dot"></span>
      <span class="wordmark__name">Morvane Equity LLC</span>
    </div>

    <div class="person">
      <h1 class="person__name">PETER DALBY</h1>
      <p class="person__title">Portfolio Manager</p>
    </div>

    <address class="address">
      2650 Birchmont Lane,<br>
      Suite 300, Atlanta GA 30327
    </address>

    <ul class="contacts">
      <li class="contacts__item">
        <svg class="contacts__icon" viewBox="0 0 12 12" aria-hidden="true">
          <path d="M2.5 1 L4.5 1 L5 3.5 L3.8 4.5 Q5 7 7.5 8.2 L8.5 7 L11 7.5 L11 9.5 Q10.5 11 9 11 Q1 10 1 3 Q1 1.5 2.5 1 Z" fill="#fff"/>
        </svg>
        <span>(412) 555-0187</span>
      </li>
      <li class="contacts__item">
        <svg class="contacts__icon" viewBox="0 0 12 12" aria-hidden="true">
          <rect x="1" y="2.5" width="10" height="7" fill="none" stroke="#fff" stroke-width="1"/>
          <path d="M1 2.5 L6 6.5 L11 2.5" fill="none" stroke="#fff" stroke-width="1"/>
        </svg>
        <span>info@morvaneequity.com</span>
      </li>
      <li class="contacts__item">
        <svg class="contacts__icon" viewBox="0 0 12 12" aria-hidden="true">
          <circle cx="6" cy="6" r="5" fill="none" stroke="#fff" stroke-width="1"/>
          <ellipse cx="6" cy="6" rx="2.2" ry="5" fill="none" stroke="#fff" stroke-width="1"/>
          <path d="M1 6 H11" stroke="#fff" stroke-width="1"/>
        </svg>
        <span>www.morvaneequity.com</span>
      </li>
    </ul>

    <div class="emblem" role="img" aria-label="Large silver-foil brand emblem area"></div>
  </section>

</main>
</body>
</html>
```